Can design for new all natural low calorie spiked lemonade

We need a clean but catchy can design for a new spiked lemonade that will be all natural, gluten free and low in calories. Open to any creative ideas ranging from designs such as using a lemonade stand to simple designs such as the example pictures that are uploaded. Looking for a can that just pops out right away on the shelf but also believe less is more as far as simplicity. The beverage is called Brightwell Spiked Lemonade, that features 3 flavors. Traditional Lemonade, Peach Lemonade and lastly Strawberry Lemonade.

Target Market(s)

21-55 years of age. 75% female, 25% male.

Colors

Designer to choose colors to be used in the design.

Requirements
Must have
• The brand name is Brightwell and it is a spiked lemonade so that should be catchy so the consumer knows what it is on first glance. Must say gluten free, all natural, and 150 calories on the front of the can. Would like some type of image on the front middle of the can. There are 3 flavors so the can should blend well with each fruit but not be different cans

```html
<!DOCTYPE html>
<html lang="en">
<head>
<meta charset="utf-8">
<title>Brightwell Spiked Lemonade – Can Label</title>
<link rel="stylesheet" href="https://fonts.googleapis.com/css2?family=Kaushan+Script&family=Michroma&display=swap">
<style>
  :root {
    --backdrop: #e9ebec;
    --lemon: #f6df2c;
    --lemon-light: #fbee6a;
    --lemon-deep: #f1c81a;
    --ink: #111111;
    --night: #1a1a1a;
    --night-soft: #3a3a38;
    --silver-light: #e4eef2;
    --silver-dark: #9fb0b8;
    --white: #ffffff;
  }
  * { margin: 0; padding: 0; box-sizing: border-box; }
  html, body {
    width: 1200px; height: 1200px; overflow: hidden;
    background: var(--backdrop);
  }
  .canvas { position: relative; width: 1200px; height: 1200px; }
  .label {
    position: absolute; left: 320px; top: 80px;
    width: 560px; height: 1040px; overflow: hidden;
  }
  .label-art { position: absolute; inset: 0; }
  .flavor-band {
    position: absolute; top: 0; left: 0; width: 100%; height: 70px;
    display: flex; align-items: center; justify-content: center;
    font-family: "Michroma", sans-serif; font-size: 24px;
    color: #2b3337; letter-spacing: 1px; text-transform: uppercase;
  }
  .brand-name {
    position: absolute; top: 150px; left: 0; width: 100%;
    text-align: center;
    font-family: "Kaushan Script", cursive; font-size: 104px;
    color: var(--ink); line-height: 1;
  }
  .spiked {
    position: absolute; top: 450px; left: 0; width: 100%;
    text-align: center;
    font-family: "Kaushan Script", cursive; font-size: 84px;
    color: var(--ink); line-height: 1;
  }
  .fruit-art {
    position: absolute; top: 560px; left: 130px; width: 320px; height: 128px;
    border-radius: 64px;
    background: radial-gradient(circle at 65% 45%, #ffd63a, #f4b417 70%, #e59e12);
  }
  .product-name {
    position: absolute; top: 700px; left: 40px; width: 480px;
    text-align: center;
    font-family: "Kaushan Script", cursive; font-size: 104px;
    color: var(--ink); line-height: 1;
    background: var(--lemon); padding: 6px 0;
    border-radius: 60px;
  }
  .claims {
    position: absolute; top: 905px; left: 0; width: 100%;
    display: flex; justify-content: space-between; padding: 0 14px;
    font-family: "Michroma", sans-serif; font-size: 23px;
    color: var(--white); text-transform: uppercase;
  }
  .calories {
    position: absolute; top: 968px; left: 0; width: 100%;
    text-align: center;
    font-family: "Michroma", sans-serif; font-size: 23px;
    color: var(--white); text-transform: uppercase;
  }
</style>
</head>
<body>
<main class="canvas">
  <section class="label">
    <svg class="label-art" width="560" height="1040" viewBox="0 0 560 1040" aria-hidden="true">
      <defs>
        <linearGradient id="silverBand" x1="0" y1="0" x2="1" y2="0">
          <stop offset="0" stop-color="var(--silver-dark)"/>
          <stop offset="0.5" stop-color="var(--silver-light)"/>
          <stop offset="1" stop-color="var(--silver-dark)"/>
        </linearGradient>
        <radialGradient id="lemonField" cx="0.5" cy="0.35" r="0.7">
          <stop offset="0" stop-color="var(--lemon-light)"/>
          <stop offset="1" stop-color="var(--lemon-deep)"/>
        </radialGradient>
        <linearGradient id="nightField" x1="0" y1="0" x2="1" y2="1">
          <stop offset="0" stop-color="var(--night-soft)"/>
          <stop offset="0.5" stop-color="var(--night)"/>
          <stop offset="1" stop-color="var(--night-soft)"/>
        </linearGradient>
      </defs>
      <rect x="0" y="0" width="560" height="70" fill="url(#silverBand)"/>
      <rect x="0" y="70" width="560" height="970" fill="url(#lemonField)"/>
      <path d="M0,560 Q300,520 560,700 L560,1040 L0,1040 Z" fill="url(#nightField)"/>
      <path class="brand-swash" d="M60,332 Q300,305 505,282" fill="none" stroke="var(--ink)" stroke-width="11" stroke-linecap="round"/>
    </svg>
    <div class="flavor-band">Traditional Lemonade</div>
    <div class="brand-name">Brightwell</div>
    <div class="spiked">spiked</div>
    <div class="fruit-art" role="img" aria-label="Illustration of whole and sliced lemons with green leaves"></div>
    <div class="product-name">Lemonade</div>
    <div class="claims"><span>Gluten Free</span><span>All Natural</span></div>
    <div class="calories">150 Calories</div>
  </section>
</main>
</body>
</html>
```